Art Wall - Illustrates "Be Colorful"

I have a seasonal color business called Willow Gate Blooms. We plant containers and add colorful annuals to garden beds. I need a 6' tall by 18' long banner that will be hung on a wall or possibly used on the side of my enclosed trailer. The banner will be used as backdrop for ladies taking pictures together and as a backdrop for colorful container gardens to be photographed for our website. It should have the words "Be Colorful" on it. I would like for it to look like a fun art wall that you would take a picture in front of in a downtown area. The art should work well with our logo. We love flowers but other ideas are welcome. Feel free to look at our instagram @willowgatebloomsokc to see examples of our work. I have uploaded our logo and a colorful flower picture we liked (great colors) but didn't quite work with our logo and a fun colorful wall at a restaurant that we really like.

Target Market(s)

women ages 30-45, wealthy, like to feel like they are trendy

Industry/Entity Type

Landscape Gardening

Font styles to use
Serif

Requirements
Must have
• The words "Be Colorful" on it and some space that would good for people to stand or objects to be placed to be photographed.
Nice to have
• We really like the colors in the "sun and skip" t-shirt picture I have attached. Also like the watercolor, alcohol ink, or hand-painted look.
Should not have
• Please do not include our logo on the banner. It will be added as a watermark to our photos.

Please do not literally use the logo flower in the design. Feel free to use pieces or inspiration from the logo but the wall should look more like art and less like a cartoon.

```html
<!DOCTYPE html>
<html lang="en">
<head>
<meta charset="utf-8">
<title>Be Colorful – Art Wall Banner</title>
<link rel="stylesheet" href="https://fonts.googleapis.com/css2?family=Caprasimo&family=Kaushan+Script&display=swap">
<style>
  :root {
    --slate: #4a5a5c;
    --tile: #ebe8dc;
    --paper: #efece4;
    --mustard: #d6a935;
    --poppy: #d24b3d;
    --sage-pale: #b4c3b7;
    --blush: #eed8c8;
    --olive: #4b5d37;
    --wash-yellow: #e7c65a;
    --wash-red: #de5b4a;
    --wash-moss: #7d8a68;
    --wash-taupe: #a99a8b;
    --wash-green: #6c875c;
    --white: #ffffff;
  }
  * { margin: 0; padding: 0; box-sizing: border-box; }
  html, body { width: 1200px; height: 539px; overflow: hidden; background: var(--slate); }
  .canvas { position: relative; width: 1200px; height: 539px; background: var(--slate); }

  .swatch {
    position: absolute; top: 42px; height: 61px;
    background: var(--tile); overflow: hidden;
    font-family: "Caprasimo", serif; font-size: 52px; line-height: 61px;
    text-align: center; white-space: nowrap;
  }
  .swatch--1 { left: 170px; width: 91px; color: var(--mustard); }
  .swatch--2 { left: 505px; width: 50px; color: var(--poppy); }
  .swatch--3 { left: 739px; width: 40px; color: var(--sage-pale); }
  .swatch--4 { left: 910px; width: 34px; color: var(--blush); }
  .swatch--5 { left: 1017px; width: 34px; color: var(--olive); }

  .banner {
    position: absolute; left: 131px; top: 121px; width: 950px; height: 316px;
    background: var(--paper); overflow: hidden;
  }
  .banner__wash {
    position: absolute; inset: 12px 0 14px 0;
    background: linear-gradient(90deg,
      var(--wash-yellow) 0%, var(--wash-yellow) 24%,
      var(--wash-red) 36%, var(--wash-red) 50%,
      var(--wash-moss) 64%, var(--wash-taupe) 80%,
      var(--wash-green) 92%, var(--wash-green) 100%);
    opacity: 0.9;
    filter: blur(2px);
  }
  .banner__title {
    position: absolute; left: 0; right: 0; top: 108px;
    text-align: center; color: var(--white);
    font-family: "Kaushan Script", cursive; font-size: 80px; line-height: 1;
    padding-right: 10px;
  }
</style>
</head>
<body>
  <main class="canvas">
    <div class="swatch swatch--1">su</div>
    <div class="swatch swatch--2">n</div>
    <div class="swatch swatch--3">a</div>
    <div class="swatch swatch--4">k</div>
    <div class="swatch swatch--5">p</div>

    <section class="banner">
      <div class="banner__wash" role="img" aria-label="Hand-painted watercolor strokes blending from mustard yellow through poppy red to moss, taupe and sage green, with a faint outlined floral motif"></div>
      <h1 class="banner__title">Be Colorful</h1>
    </section>
  </main>
</body>
</html>
```